Chamber of Commerce Web Design Project

We are working with Harborvale Chamber of Commerce. They are a new chamber of commerce forming in SoCal.
Some sites to use for inspiration:
https://brindlemarchamber.org
https://vantrelo.org
https://www.quarrowfieldchamber.com
https://www.tjchamber.com
https://morwenpaccc.org
Thank you for taking the time to consider designing a website for us. We are web developers based in Stockton, CA, USA. Most of our projects go through the same process. Understanding this process may help you win a project with us. We custom-code all of our websites in-house. We don’t have any requirements as to what tools you use for your design, but we prefer Figma files. For any design that we label as four-stars, we send it to the client for review. The client picks the final design they want us to use. Once we complete this process, we will continue to show additional clients all the four-star sites and purchase them later. Your designs will have multiple chances to sell. For better chances of success, we ask that you follow these guidelines.
IMAGES:
If you use any images or icons in the design, we ask that you have a link to the asset so we can purchase the image/icon. Most of the designs we submit do not have the customer’s images on them unless they have some great images. Be creative; show us the feeling you are trying to portray with your image choices. Use any royalty-free site you choose. We subscribe to Adobe and mainly use their images, but we can purchase images outside of Adobe.
PLEASE NOTE: we will not submit designs to clients with watermarks on the images.
FONTS:
We ask that you identify the fonts used in the design. This can be done in a message if you want. We typically use Google Fonts and Adobe Fonts.
CONTENT:
We're always open to different content and ideas. We often submit designs with stock images so the client can see our vision. We typically take pictures after the website launch to use their images with our vision. Lorem Ipsum is fine for paragraphs, but we ask that you write the headers in correct English. We want to be able to show the vision and identify the sections of the website.
INSPIRATION:
We typically add a couple of links in the brief of websites we like to help you get started in your design.
REVISIONS:
We do not often ask for revisions of the designs unless we see something in the design that may not appeal to the client. If there are slight changes that we want to make, we do that in the development process.
FEEDBACK:
We rarely give feedback on designs during the design process. We are working on many website projects and do not have the time to provide feedback. We usually respond if your request is well thought out and asks specific questions, but a note asking “feedback, please” usually goes unanswered.

```html
<!DOCTYPE html>
<html lang="en">
<head>
<meta charset="utf-8">
<title>Harborvale Chamber of Commerce</title>
<link href="https://fonts.googleapis.com/css2?family=Montserrat:wght@400;500;600;700;800&display=swap" rel="stylesheet">
<style>
:root{
  --stage:#cfcfcf;
  --white:#ffffff;
  --brand:#1a8cff;
  --band:#0a72c4;
  --navy:#1d3a5a;
  --deep:#13304d;
  --ink:#2d3a4a;
  --muted:#6b7684;
  --yellow:#f7c22e;
  --orange:#f39422;
  --soft:#eef2f6;
  --line:#c9d2dc;
}
*{box-sizing:border-box;margin:0;padding:0}
html,body{width:1200px;height:1200px;overflow:hidden}
body{background:var(--stage);font-family:"Montserrat",sans-serif;color:var(--ink);position:relative}
.page{position:absolute;left:424px;top:38.5px;width:564px;height:1808px;background:var(--white);transform:scale(0.6211);transform-origin:0 0;overflow:hidden}
.abs{position:absolute}
.img{position:absolute}
/* header */
.brand{left:35px;top:10px;display:flex;align-items:center;gap:3px;font-weight:800;font-size:10.5px;color:var(--brand);white-space:nowrap}
.brand .dot{width:11px;height:11px;border-radius:50%;background:var(--yellow)}
.follow{left:250px;top:6px;display:flex;align-items:center;gap:2px;font-size:3.5px;font-weight:700;color:var(--navy)}
.soc-sm{width:8px;height:8px;border-radius:50%;border:1px solid var(--navy)}
.hline{left:118px;top:16px;width:310px;height:1px;background:var(--line)}
.nav{left:160px;top:20px;display:flex;gap:10px;font-size:6px;color:var(--muted)}
.nav .on{color:var(--brand);border-top:1px solid var(--brand)}
.login{left:447px;top:14px;font-size:5.5px;font-weight:700;color:var(--navy)}
.btn-top{left:470px;top:10px;width:58px;height:17px;background:var(--brand);color:#fff;font-size:4.5px;display:flex;align-items:center;justify-content:center}
.search{left:535px;top:13px}
/* hero */
.hero{left:0;top:35px;width:564px;height:182px;background:linear-gradient(180deg,#3c5876 0%,#2a4563 60%,#1d3048 100%)}
.hero h1{position:absolute;left:88px;top:36px;font-size:26px;line-height:30px;font-weight:700;color:#fff;letter-spacing:2px}
.hero h1 span{color:var(--brand);display:block}
.btn-ghost{border:1.5px solid #fff;color:#fff;display:flex;align-items:center;justify-content:center}
.arrow{width:22px;height:22px;border-radius:50%;background:#fff;display:flex;align-items:center;justify-content:center;top:80px}
/* investors */
.inv{top:228px;width:86px;height:33px;border:1.5px solid #9aa3ad;font-size:10px;line-height:10px;text-align:center;padding-top:6px;color:#333}
.dots{left:277px;top:273px;display:flex;gap:2px}
.dots i{width:2px;height:2px;border-radius:50%;background:var(--brand);display:block}
/* bands */
.band{left:0;width:564px;background:var(--band)}
.band-title{font-size:9px;line-height:10.5px;font-weight:700;color:#fff}
.band-text{font-size:6.6px;line-height:10px;color:#e4f0fb}
.play{left:367px;top:327px;width:36px;height:36px;border-radius:50%;border:3px solid var(--yellow);background:var(--orange);display:flex;align-items:center;justify-content:center}
/* about */
.h2{font-size:11px;font-weight:700;color:var(--band)}
.para{font-size:7px;line-height:10px;color:#555}
.btn-yel{background:var(--yellow);border-radius:10px;color:var(--navy);font-size:6.3px;font-weight:600;display:flex;align-items:center;justify-content:center;gap:4px}
/* program */
.card{width:184px;height:81px;border:1px solid #d9dee4;border-radius:4px;background:#fff;box-shadow:0 2px 4px rgba(0,0,0,.12);padding:7px}
.card.hot{background:linear-gradient(100deg,var(--orange),#f9c230);border:none}
.ico{width:26px;height:26px;border-radius:4px;background:var(--band);display:flex;align-items:center;justify-content:center}
.hot .ico{background:rgba(255,255,255,.3)}
.card h4{margin-top:4px;font-size:5.8px;font-weight:600;color:var(--band)}
.card p{font-size:5px;line-height:6.2px;color:#555}
.hot h4,.hot p{color:#fff}
/* benefits */
.ben{left:90px;display:flex;align-items:center;gap:5px;font-size:6.5px;line-height:10px;color:#555;width:200px}
.tick{flex:none;width:12px;height:12px;border-radius:50%;background:var(--yellow);display:flex;align-items:center;justify-content:center}
/* testimonials */
.testi{left:0;top:1199px;width:566px;height:176px;background:linear-gradient(90deg,#2d4d6b,#19567c 40%,#1c5578 70%,#2b4965)}
.stat{top:1329px;width:71px;height:35px;border-radius:3px;background:#1b78a6;text-align:center;padding-top:10px;font-size:4px;color:#fff}
.stat b{display:block;font-size:4.2px;border-bottom:.5px solid rgba(255,255,255,.5);margin:0 8px 4px;padding-bottom:2px}
.stat.on{background:var(--yellow);color:var(--navy)}
/* blog */
.bcard{background:var(--soft)}
.bcard .pic{width:100%;background:linear-gradient(120deg,#8a8f8c,#c7c2b2 50%,#6d7775)}
.bsmall{width:87px;height:93px}
.bsmall .pic{height:47px}
.bsmall h5{font-size:6.4px;line-height:10px;font-weight:500;color:#333;padding:2px 5px 0}
.bsmall small{display:block;font-size:4.5px;color:#9aa3ad;padding:2px 5px}
/* footer */
.footer{left:0;top:1626px;width:564px;height:182px;background:linear-gradient(180deg,#2c4a68,#1e3550 60%,#15263a)}
.fcol h6{font-size:8.5px;font-weight:700;color:#fff;margin-bottom:15px}
.fcol a{display:block;font-size:4.6px;color:#cdd7e2;margin-bottom:9px;text-decoration:none}
.soc{width:21px;height:21px;border-radius:50%;border:1.3px solid #fff;top:1744px}
</style>
</head>
<body>
<div class="page">

  <!-- header -->
  <div class="abs brand"><span class="dot"></span>HARBORVALE</div>
  <div class="abs follow">Follow Us: <span class="soc-sm"></span><span class="soc-sm"></span><span class="soc-sm"></span><span class="soc-sm"></span></div>
  <div class="abs hline"></div>
  <nav class="abs nav"><span class="on">Home ▾</span><span>About Us ▾</span><span>Membership ▾</span><span>Events ▾</span><span>News ▾</span><span>Contact Us</span></nav>
  <div class="abs login">Log in</div>
  <div class="abs btn-top">Become a Member</div>
  <svg class="abs search" width="9" height="9" viewBox="0 0 10 10"><circle cx="4" cy="4" r="3" fill="none" stroke="#9aa3ad" stroke-width="1"/><path d="M6.3 6.3L9 9" stroke="#9aa3ad" stroke-width="1"/></svg>

  <!-- hero -->
  <section class="abs hero" role="img" aria-label="City skyline at dusk above a waterfront pier">
    <h1><span>HARBORVALE</span>CHAMBER OF<br>COMMERCE</h1>
    <div class="abs btn-ghost" style="left:88px;top:140px;width:66px;height:18px;font-size:7px">Join Now</div>
    <div class="abs arrow" style="left:-1px"><svg width="6" height="8" viewBox="0 0 6 8"><path d="M4.5 1L1.5 4l3 3" fill="none" stroke="#333"/></svg></div>
    <div class="abs arrow" style="left:542px"><svg width="6" height="8" viewBox="0 0 6 8"><path d="M1.5 1l3 3-3 3" fill="none" stroke="#333"/></svg></div>
  </section>

  <!-- investors -->
  <div class="abs inv" style="left:89px">Logo<br>Investors</div>
  <div class="abs inv" style="left:186px">Logo<br>Investors</div>
  <div class="abs inv" style="left:284px">Logo<br>Investors</div>
  <div class="abs inv" style="left:381px">Logo<br>Investors</div>
  <div class="abs dots"><i></i><i></i><i></i></div>

  <!-- network band -->
  <section class="abs band" style="top:283px;height:115px">
    <h3 class="abs band-title" style="left:88px;top:13px;width:208px">Building a Strong Business Network through Harborvale Chamber of Commerce</h3>
    <p class="abs band-text" style="left:88px;top:42px;width:200px;color:#0c2c4a">Building a strong business network through Harborvale Chamber of Commerce, connecting you with professionals and businesses in the pipeline industry.</p>
    <div class="abs btn-ghost" style="left:89px;top:76px;width:79px;height:17px;font-size:6px">Become a Member</div>
    <div class="abs" style="left:298px;top:0;width:171px;height:115px;background:linear-gradient(135deg,#c9d3dc,#7f8d99 55%,#4e5a66)" role="img" aria-label="Business meeting in a bright conference room"></div>
  </section>
  <div class="abs play"><svg width="12" height="14" viewBox="0 0 12 14"><path d="M1 1l10 6-10 6z" fill="#fff"/></svg></div>

  <!-- about -->
  <div class="img" style="left:89px;top:420px;width:205px;height:196px;background:linear-gradient(160deg,#b9c4cf,#6d7f93 50%,#26344a)" role="img" aria-label="Three business professionals standing in front of an office building"></div>
  <h2 class="abs h2" style="left:306px;top:425px">About Us</h2>
  <p class="abs para" style="left:306px;top:440px;width:162px">Lorem ipsum dolor sit amet, consectetuer adipiscing elit, sed diam nonummy nibh euismod tincidunt ut laoreet dolore magna aliquam erat volutpat. Ut wisi enim ad minim veniam, quis nostrud exerci tation ullamcorper suscipit lobortis nisl ut aliquip ex ea commodo consequat. Duis autem vel eum iriure dolor in hendrerit in vulputate velit esse molestie consequat, vel illum dolore eu feugiat nulla facilisis at vero eros et accumsan et iusto odio dignissim qui blandit praesent luptatum zzril delenit augue duis dolore te feugait nulla facilisi.</p>
  <div class="abs btn-yel" style="left:306px;top:580px;width:76px;height:19px">Learn More <svg width="9" height="5" viewBox="0 0 9 5"><path d="M0 2.5h8M6 .5l2 2-2 2" fill="none" stroke="#1d3a5a" stroke-width=".8"/></svg></div>

  <!-- program -->
  <h2 class="abs" style="left:0;width:564px;top:637px;text-align:center;font-size:11px;font-weight:600;color:#444">Our <span style="color:var(--band);font-weight:700">Program</span></h2>
  <p class="abs para" style="left:88px;top:652px;width:384px;text-align:center">Lorem ipsum dolor sit amet, consectetuer adipiscing elit, sed diam nonummy nibh euismod tincidunt ut laoreet dolore magna</p>

  <div class="abs card hot" style="left:89px;top:679px">
    <div class="ico"><svg width="14" height="14" viewBox="0 0 14 14" fill="none" stroke="#fff" stroke-width="1"><circle cx="7" cy="3" r="2"/><circle cx="3" cy="10" r="2"/><circle cx="11" cy="10" r="2"/><path d="M6 5L4 8M8 5l2 3M5 10h4"/></svg></div>
    <h4>Business Networking</h4>
    <p>A program that enables members to interact and collaborate with fellow members, building a strong professional network.</p>
  </div>
  <div class="abs card" style="left:284px;top:679px">
    <div class="ico"><svg width="14" height="14" viewBox="0 0 14 14" fill="none" stroke="#fff" stroke-width="1.2"><path d="M2 13V9M6 13V6M10 13V3M1 6l4-3 3 2 4-4"/></svg></div>
    <h4>Career Development</h4>
    <p>A program providing training, seminars, and workshops to help members develop their careers and enhance their professional skills.</p>
  </div>
  <div class="abs card" style="left:89px;top:768px">
    <div class="ico"><svg width="14" height="14" viewBox="0 0 14 14"><circle cx="7" cy="7" r="6" fill="#fff"/><path d="M4 7l2 2 4-4" fill="none" stroke="#0a72c4" stroke-width="1.3"/></svg></div>
    <h4>Industry Advocacy</h4>
    <p>A program representing the interests of the pipeline industry in regulatory, policy, and other issues, promoting the industry and environmental safety.</p>
  </div>
  <div class="abs card" style="left:284px;top:768px">
    <div class="ico"><svg width="14" height="14" viewBox="0 0 14 14" fill="none" stroke="#fff" stroke-width="1.1"><path d="M7 2a3.5 3.5 0 0 0-2 6.4V10h4V8.4A3.5 3.5 0 0 0 7 2zM5.5 12h3M7 0v1M1 5h1M12 5h1"/></svg></div>
    <h4>Conferences and Seminars</h4>
    <p>A program hosting conferences and seminars on topics relevant to the pipeline industry, enabling members to gain knowledge and stay updated on industry developments.</p>
  </div>

  <!-- event -->
  <section class="abs band" style="top:862px;height:135px">
    <div class="abs" style="left:89px;top:0;width:201px;height:135px;background:radial-gradient(circle at 60% 30%,#9fd2ff 0%,#2f6fc0 30%,#12305e 75%)" role="img" aria-label="Audience seated at a conference hall facing a lit stage"></div>
    <div class="abs" style="left:306px;top:10px;font-size:6px;color:#fff">Featured Event</div>
    <h3 class="abs" style="left:306px;top:22px;font-size:11.5px;font-weight:700;color:#fff">Business Expo 2025</h3>
    <p class="abs band-text" style="left:306px;top:37px;width:172px;line-height:12px">We are proud to present the Business Expo 2024, our largest annual event that brings together local businesses, industry leaders, and the community to share ideas, build connections, and promote economic growth.</p>
    <div class="abs btn-yel" style="left:306px;top:104px;width:76px;height:19px">See More <svg width="9" height="5" viewBox="0 0 9 5"><path d="M0 2.5h8M6 .5l2 2-2 2" fill="none" stroke="#1d3a5a" stroke-width=".8"/></svg></div>
  </section>

  <!-- benefits -->
  <h2 class="abs" style="left:90px;top:1013px;font-size:11px;font-weight:600;color:#555">Benefits <span style="color:var(--band);font-weight:700">of Membership</span></h2>
  <p class="abs para" style="left:90px;top:1030px;width:180px">As a member of the Harborvale Chamber of Commerce, you will receive:</p>
  <div class="abs ben" style="top:1061px"><span class="tick"><svg width="7" height="5" viewBox="0 0 7 5"><path d="M.7 2.5l2 1.8L6.3.7" fill="none" stroke="#fff" stroke-width="1"/></svg></span>Access to a wide network of businesses</div>
  <div class="abs ben" style="top:1085px"><span class="tick"><svg width="7" height="5" viewBox="0 0 7 5"><path d="M.7 2.5l2 1.8L6.3.7" fill="none" stroke="#fff" stroke-width="1"/></svg></span>Opportunities to promote your business through our events and activities</div>
  <div class="abs ben" style="top:1116px"><span class="tick"><svg width="7" height="5" viewBox="0 0 7 5"><path d="M.7 2.5l2 1.8L6.3.7" fill="none" stroke="#fff" stroke-width="1"/></svg></span>Access to up-to-date business resources and information</div>
  <div class="abs ben" style="top:1145px"><span class="tick"><svg width="7" height="5" viewBox="0 0 7 5"><path d="M.7 2.5l2 1.8L6.3.7" fill="none" stroke="#fff" stroke-width="1"/></svg></span>A voice in advocacy for business and community interests in the Harborvale area</div>
  <div class="abs" style="left:89px;top:1175px;font-size:6.5px;font-weight:600;color:var(--band)">Learn More &nbsp;→</div>
  <div class="img" style="left:290px;top:1010px;width:180px;height:158px;background:linear-gradient(160deg,#e6e8ea,#b8bec6 45%,#243048)" role="img" aria-label="Three smiling businessmen in suits"></div>

  <!-- testimonials -->
  <section class="abs testi" role="img" aria-label="Industrial pipe facility in blue tones behind testimonials">
    <div class="abs" style="left:90px;top:20px;font-size:10.5px;color:#fff">Our <span style="color:var(--brand)">Testimonials</span></div>
    <h3 class="abs" style="left:90px;top:40px;width:150px;font-size:10.5px;line-height:13px;font-weight:700;color:#fff">Achieving Success with <span style="color:var(--brand)">Harborvale</span> Chamber of Commerce</h3>
    <div class="abs btn-ghost" style="left:89px;top:88px;width:80px;height:17px;font-size:6px">Become a Member</div>
    <div class="abs" style="left:245px;top:17px;width:93px;height:109px;background:linear-gradient(160deg,#d5dde3,#5d6d82 55%,#1f2c40)" role="img" aria-label="Smiling executive holding a tablet"></div>
    <div class="abs" style="left:440px;top:14px;font-size:18px;font-weight:700;color:#2d5f86">”</div>
    <p class="abs" style="left:348px;top:34px;width:120px;font-size:6.8px;line-height:9.8px;color:#fff">"Membership with Harborvale Chamber of Commerce has helped me expand my business network and stay informed about the pipeline industry."</p>
    <div class="abs" style="left:348px;top:91px;font-size:5px;font-weight:700;color:#fff">Jordan Reyes<br><span style="font-weight:400;font-size:4px">CEO, Harborvale Inc.</span></div>
    <div class="abs" style="left:349px;top:111px;font-size:6px;color:var(--yellow)">◀ &nbsp;▶</div>
  </section>
  <div class="abs stat on" style="left:167px"><b>Membership</b>987+ Membership reviews</div>
  <div class="abs stat" style="left:247px"><b>Investment</b>100+ Investors reviews</div>
  <div class="abs stat" style="left:327px"><b>Partners</b>120+ Partners reviews</div>

  <!-- blog -->
  <div class="abs" style="left:0;width:564px;top:1385px;text-align:center;font-size:6.5px;color:var(--brand)">Featured Article</div>
  <h2 class="abs" style="left:0;width:564px;top:1393px;text-align:center;font-size:11px;font-weight:600;color:#555">Latest from Our Blog</h2>

  <article class="abs bcard" style="left:89px;top:1409px;width:182px;height:196px">
    <div class="pic" style="height:85px" role="img" aria-label="Engineer in a hard hat inspecting pipes"></div>
    <small style="display:block;font-size:4.5px;color:#9aa3ad;padding:5px 13px 0">Jan 8, 2025</small>
    <h5 style="font-size:7.5px;line-height:10.5px;font-weight:500;color:#333;padding:5px 13px 0">The Future of the Pipeline Industry: Challenges and Opportunities</h5>
    <p style="font-size:4.5px;line-height:6.5px;color:#9aa3ad;padding:6px 13px 0">The Harborvale Chamber of Commerce discusses the future of the pipeline industry and how we can address challenges and capitalize on opportunities.</p>
    <div style="margin:10px 13px 0;height:19px;background:#fff;border:1px solid #dde3e9;font-size:7px;color:var(--brand);display:flex;align-items:center;justify-content:center">Read More</div>
  </article>
  <article class="abs bcard bsmall" style="left:280px;top:1409px"><div class="pic" role="img" aria-label="Engineer checking pipeline valves"></div><h5>Innovative Technologies in the Pipeline Industry</h5><small>Jan 8, 2025</small></article>
  <article class="abs bcard bsmall" style="left:381px;top:1409px"><div class="pic" role="img" aria-label="Engineer checking pipeline valves"></div><h5>The Importance of Networking in Pipeline Business</h5><small>Jan 8, 2025</small></article>
  <article class="abs bcard bsmall" style="left:280px;top:1512px"><div class="pic" role="img" aria-label="Engineer checking pipeline valves"></div><h5>Latest Trends in the Pipeline Industry</h5><small style="padding-top:12px">Jan 8, 2025</small></article>
  <article class="abs bcard bsmall" style="left:381px;top:1512px"><div class="pic" role="img" aria-label="Engineer checking pipeline valves"></div><h5>Innovative Technologies in the Pipeline Industry</h5><small>Jan 8, 2025</small></article>

  <!-- footer -->
  <footer class="abs footer" role="img" aria-label="Evening city skyline and pier in dark blue">
    <div class="abs" style="left:93px;top:42px;display:flex;align-items:center;gap:4px;font-size:13px;font-weight:800;color:var(--brand);white-space:nowrap"><span style="width:16px;height:16px;border-radius:50%;background:var(--yellow)"></span>HARBORVALE</div>
    <div class="abs" style="left:93px;top:80px;width:91px;height:26px;border-bottom:1px solid #fff;font-size:5px;color:#fff;padding-top:13px">Enter email</div>
    <div class="abs" style="left:184px;top:80px;width:29px;height:26px;background:var(--yellow);font-size:5px;color:var(--navy);display:flex;align-items:center;justify-content:center">Send</div>
    <div class="abs fcol" style="left:234px;top:44px"><h6>Company Policy</h6><a>Terms and Conditions</a><a>Privacy Policy</a><a>Cookie Policy</a><a style="font-weight:700;color:#fff;font-size:5px">Connect with us!</a><a>support@harborvale.example</a></div>
    <div class="abs fcol" style="left:336px;top:44px"><h6>Company</h6><a>Become a Partner (coming 2025)</a><a>Careers</a><a>About Us</a><a>Blog</a></div>
    <div class="abs fcol" style="left:434px;top:44px"><h6>Services</h6><a>Services</a><a>Membership</a><a>Event</a><a>News</a></div>
    <div class="abs" style="left:0;width:564px;top:163px;text-align:center;font-size:5px;color:#fff">@Copyright 2025 Harborvale Chamber of Commerce. <span style="color:var(--brand)">All Rights Reserved.</span></div>
  </footer>
  <div class="abs soc" style="left:91px"></div>
  <div class="abs soc" style="left:115px"></div>
  <div class="abs soc" style="left:139px"></div>
  <div class="abs soc" style="left:163px"></div>

  <div class="abs" style="left:210px;top:1612px;width:169px;height:28px;border-radius:14px;background:linear-gradient(90deg,var(--yellow),#f9b92a);color:#fff;font-size:6.5px;font-weight:600;display:flex;align-items:center;justify-content:center">Join Now and Unlock Member Benefits</div>

</div>
</body>
</html>
```